Book Title: “Ember: Road of Quiet Dawn” Please see the attachment “Text on the cover”.

Book Cover Design Instructions: This book is meant for people of all religions and nationalities. Therefore, on the cover, there should be no mosque or an object specific to any religion. The primary emphasis should be on the "unconditional love of God." Therefore, use universal symbols of love. The second priority themes could be Sufism, Peace, and self-improvement. Rest is your imagination. Please also see the attachment: 'Book description and author's Bio.'
This book has the potential to be a best seller. Please do a good job.
What Book Cover Formats are required: A designer should submit cover designs in three formats: (1) eBook, (2) Paperback, and (3) Hardback. These books will be published on Velmora PBX.
Format requirements for eBooks are available from: https://pbx.velmora-press.example/en_US/help/topic/R731928405.
You can find paperback and hardback cover measurements from: https://pbx.velmora-press.example/en_US/cover-calculator
• To complete the project, all three formats should be accepted by Velmora PBX.
• The book interior trim size is 6.14 X 9.21 inches.
• Interior Type: Premium color.
• No bleed.
• I do not upload barcode. So, the back cover should have room for Velmora to print the barcode.
• Number of pages 126.
Compensation for the designer: After selecting one designer, I will increase the amount by $200 on Artlumo to compensate for three deliverables.
Follow-up of the Project:
After the book is published, I may need minor revisions. For example, the number of pages may change. Therefore, I will need the same design in revised sizes. In that case, I will pay $25 for each revision. For example, if the number of pages changes, I will need a different spine for paperback and hardback, then I will pay the artist $25 + $25 = $50 for both designs.
List of Enclosers:
1. Text on the cover.
2. Book description and author's Bio for the back cover.
3. Later, I will upload my picture for the book's back cover.

Target Market(s)

Any adult

Industry/Entity Type

Any industry

Requirements
Must have
• Three Deliverables

```html
<!DOCTYPE html>
<html lang="en">
<head>
<meta charset="utf-8">
<title>Ember: Road of Quiet Dawn — Cover Options</title>
<link href="https://fonts.googleapis.com/css2?family=Playfair+Display:wght@700&family=Raleway:ital,wght@0,300;0,400;0,500;1,300&family=Poppins:wght@600&display=swap" rel="stylesheet">
<style>
  :root {
    --canvas: #7a7a7a;
    --spine: #1d1f2b;
    --ink-dark: #111111;
    --ink-light: #f4f4f4;
    --dawn-top: #d7e9ee;
    --dawn-mid: #f3e4d2;
    --dawn-low: #f0a45a;
    --night: #0a0a0a;
    --navy: #132548;
    --box: #ffffff;
    --muted: #9a9a9a;
  }
  * { box-sizing: border-box; margin: 0; padding: 0; }
  html, body { width: 1200px; height: 2520px; overflow: hidden; background: var(--canvas); }
  .cover {
    position: absolute; left: 49px; width: 1102px; height: 813px; overflow: hidden;
  }
  .cover--dawn { top: 29px; }
  .cover--night { top: 859px; }
  .cover--stars { top: 1689px; }

  .back { position: absolute; left: 0; top: 0; width: 538px; height: 100%; font-family: "Raleway", sans-serif; }
  .cover--dawn .back { background: linear-gradient(180deg, #d9ecef 0%, #eef0ea 50%, #f7e9dd 100%); color: var(--ink-dark); }
  .cover--night .back { background: var(--night); color: var(--ink-light); }
  .cover--stars .back { background: var(--navy); color: var(--ink-light); }

  .back__title { position: absolute; top: 55px; left: 0; width: 100%; text-align: center;
    font-family: "Playfair Display", serif; font-weight: 700; font-size: 29px; line-height: 33px; }
  .back__subtitle { position: absolute; top: 133px; left: 0; width: 100%; text-align: center;
    font-size: 14.5px; line-height: 17px; font-weight: 400; }
  .rule { position: absolute; left: 209px; width: 120px; height: 10px; }
  .rule--top { top: 185px; }
  .rule--bottom { top: 619px; }

  .blurb { position: absolute; top: 205px; left: 41px; width: 456px; font-size: 10.4px; line-height: 14.3px; font-weight: 300; text-align: justify; }
  .blurb p { margin-bottom: 14px; }
  .blurb ol { margin: 0 0 14px 18px; padding-left: 0; }
  .blurb li { padding-left: 4px; }

  .author-photo { position: absolute; left: 39px; top: 678px; width: 84px; height: 84px; border-radius: 50%;
    background: var(--box); color: var(--muted); font-size: 10px; display: flex; align-items: center; justify-content: center; text-align: center; line-height: 14px; }
  .bio { position: absolute; left: 134px; top: 676px; width: 195px; font-size: 10.2px; line-height: 14.2px; font-weight: 300; }
  .bio strong { font-weight: 500; display: block; }
  .barcode-space { position: absolute; left: 345px; top: 677px; width: 172px; height: 104px; background: var(--box);
    color: var(--muted); font-size: 10px; display: flex; align-items: center; justify-content: center; }

  .spine { position: absolute; left: 538px; top: 0; width: 27px; height: 100%; background: var(--spine); color: #e6e6e6;
    font-family: "Raleway", sans-serif; font-size: 10.5px; letter-spacing: 0.5px; }
  .spine span { position: absolute; left: 7px; writing-mode: vertical-rl; white-space: nowrap; }
  .spine__title { top: 52px; }
  .spine__author { top: 337px; }
  .spine__year { top: 673px; }

  .front { position: absolute; left: 565px; top: 0; width: 537px; height: 100%; text-align: center; }
  .cover--dawn .front { background: #e3eef0; color: var(--ink-dark); }
  .cover--night .front { background: var(--night); color: var(--ink-light); }
  .cover--stars .front { color: var(--ink-light); }

  .art { position: absolute; }
  .cover--dawn .art { left: 0; top: 0; width: 100%; height: 100%;
    background: radial-gradient(circle at 52% 52%, #f7a24c 0 12%, rgba(247,162,76,0) 22%),
                linear-gradient(180deg, #d6eaee 0%, #ecebe1 35%, #f3d3b0 65%, #e99b5c 85%, #8c6a58 100%); }
  .cover--night .art { left: 40px; top: 199px; width: 462px; height: 466px;
    background: radial-gradient(ellipse at 50% 55%, #e9e4dc 0 14%, #d86a2a 28%, #5a2a18 48%, rgba(10,10,10,0) 70%); }
  .cover--stars .art { left: 0; top: 0; width: 100%; height: 100%;
    background: linear-gradient(180deg, #0d1426 0%, #1d2440 25%, #5a4660 45%, #a7717a 58%, #aab4cf 75%, #e4e8f2 100%); }

  .front__title { position: absolute; top: 40px; left: 0; width: 100%; font-family: "Playfair Display", serif; font-weight: 700;
    font-size: 48px; line-height: 52px; }
  .front__subtitle { position: absolute; top: 158px; left: 0; width: 100%; font-family: "Raleway", sans-serif; font-size: 17.5px; font-weight: 400; }
  .front__byline { position: absolute; left: 0; width: 100%; font-family: "Poppins", sans-serif; font-weight: 600; font-size: 15px; line-height: 20px; }
  .cover--dawn .front__byline { top: 225px; }
  .cover--night .front__byline { top: 694px; }
  .cover--stars .front__byline { top: 693px; }
</style>
</head>
<body>

<section class="cover cover--dawn">
  <div class="back">
    <h2 class="back__title">EMBER:<br>Road of Quiet Dawn</h2>
    <p class="back__subtitle">Guide to Cultivating Inner Peace<br>and Mindful Living</p>
    <svg class="rule rule--top" viewBox="0 0 120 10"><line x1="0" y1="5" x2="120" y2="5" stroke="currentColor" stroke-width="0.8"/></svg>
    <div class="blurb">
      <p>This book intricately intertwines the diverse teachings of Sufism with the deep wisdom of the Quran to create a comprehensive roadmap for personal spiritual growth. The reader has a chance to experience <em>firsthand</em> the profound peace and boundless love Sufis have cherished for centuries. This book addresses the following critical questions:</p>
      <ol>
        <li><em>How can one unconditionally love God?</em> It is the greatest of all kinds of love that ignites a profound and transformative spiritual journey.</li>
        <li><em>How to feel the love of God</em>, which can bring immense peace and contentment.</li>
        <li><em>How to unconditionally love yourself</em>, which nurtures personal growth and harmony.</li>
        <li>What is the most effective way to respond to <em>life's critical crises to reduce suffering and expedite recovery?</em></li>
      </ol>
      <p>This book also explores Islam's overwhelming emphasis on avoiding <em>Zulm</em> (oppression and injustice) because the Quran mentions the word <em>Zulm</em> an astounding 291 times. Avoiding <em>Zulm</em> in all human interactions should be the top priority for every Muslim.</p>
      <p>The sage Harun Velid did not just preach peace and love. He gave us a practical example when he took over as a ruler of the Medina <em>without bloodshed</em>. He did not inherit power through the dynasty, and Medina was multi-religious. Arguably, it was history's first large-scale peaceful transfer of power.</p>
      <p>Similarly, he signed the Treaty of Hudaybia with the staunchest enemy, employing an unprecedented peaceful strategy to <em>nonviolently</em> end a bitter war that had claimed hundreds of lives.</p>
      <p>The highlight of this book is that it points to the methodology to acquire a fully satisfied and contented soul (<em>Nafs-e-Mutma'inna</em>) in practical steps, which is the goal of every Sufi wayfarer.</p>
    </div>
    <svg class="rule rule--bottom" viewBox="0 0 120 10"><line x1="0" y1="5" x2="120" y2="5" stroke="currentColor" stroke-width="0.8"/></svg>
    <div class="author-photo">Space for<br>PHOTO</div>
    <p class="bio"><strong>Dr. Tarek Hollander</strong>Dr. Hollander holds a Master's in Physics and a Master's in Computer Science and worked as a Software Engineer. He earned his Ph.D. in Islamic Studies. He was one of the founders of a mosque in Virginia.</p>
    <div class="barcode-space">Space for BARCODE</div>
  </div>
  <div class="spine"><span class="spine__title">EMBER: ROAD OF QUIET DAWN</span><span class="spine__author">Dr. TAREK HOLLANDER</span><span class="spine__year">PUBLISHED YEAR</span></div>
  <div class="front">
    <div class="art" role="img" aria-label="Photo of cupped hands holding a glowing orange heart against a sunrise sky"></div>
    <h1 class="front__title">EMBER:<br>Road of Quiet Dawn</h1>
    <p class="front__subtitle">Guide to Cultivating Inner Peace and Mindful Living</p>
    <p class="front__byline">By<br>Dr. Tarek Hollander</p>
  </div>
</section>

<section class="cover cover--night">
  <div class="back">
    <h2 class="back__title">EMBER:<br>Road of Quiet Dawn</h2>
    <p class="back__subtitle">Guide to Cultivating Inner Peace<br>and Mindful Living</p>
    <svg class="rule rule--top" viewBox="0 0 120 10"><line x1="0" y1="5" x2="120" y2="5" stroke="currentColor" stroke-width="0.8"/></svg>
    <div class="blurb">
      <p>This book intricately intertwines the diverse teachings of Sufism with the deep wisdom of the Quran to create a comprehensive roadmap for personal spiritual growth. The reader has a chance to experience <em>firsthand</em> the profound peace and boundless love Sufis have cherished for centuries. This book addresses the following critical questions:</p>
      <ol>
        <li><em>How can one unconditionally love God?</em> It is the greatest of all kinds of love that ignites a profound and transformative spiritual journey.</li>
        <li><em>How to feel the love of God</em>, which can bring immense peace and contentment.</li>
        <li><em>How to unconditionally love yourself</em>, which nurtures personal growth and harmony.</li>
        <li>What is the most effective way to respond to <em>life's critical crises to reduce suffering and expedite recovery?</em></li>
      </ol>
      <p>This book also explores Islam's overwhelming emphasis on avoiding <em>Zulm</em> (oppression and injustice) because the Quran mentions the word <em>Zulm</em> an astounding 291 times. Avoiding <em>Zulm</em> in all human interactions should be the top priority for every Muslim.</p>
      <p>The sage Harun Velid did not just preach peace and love. He gave us a practical example when he took over as a ruler of the Medina <em>without bloodshed</em>. He did not inherit power through the dynasty, and Medina was multi-religious. Arguably, it was history's first large-scale peaceful transfer of power.</p>
      <p>Similarly, he signed the Treaty of Hudaybia with the staunchest enemy, employing an unprecedented peaceful strategy to <em>nonviolently</em> end a bitter war that had claimed hundreds of lives.</p>
      <p>The highlight of this book is that it points to the methodology to acquire a fully satisfied and contented soul (<em>Nafs-e-Mutma'inna</em>) in practical steps, which is the goal of every Sufi wayfarer.</p>
    </div>
    <div class="author-photo">Space for<br>PHOTO</div>
    <p class="bio"><strong>Dr. Tarek Hollander</strong>Dr. Hollander holds a Master's in Physics and a Master's in Computer Science and worked as a Software Engineer. He earned his Ph.D. in Islamic Studies. He was one of the founders of a mosque in Virginia.</p>
    <div class="barcode-space">Space for BARCODE</div>
  </div>
  <div class="spine"><span class="spine__title">EMBER: ROAD OF QUIET DAWN</span><span class="spine__author">Dr. TAREK HOLLANDER</span><span class="spine__year">PUBLISHED YEAR</span></div>
  <div class="front">
    <div class="art" role="img" aria-label="Illustration of a whirling dancer in white robes surrounded by swirling ribbons of orange and teal"></div>
    <h1 class="front__title">EMBER:<br>Road of Quiet Dawn</h1>
    <p class="front__subtitle">Guide to Cultivating Inner Peace and Mindful Living</p>
    <p class="front__byline">By<br>Dr. Tarek Hollander</p>
  </div>
</section>

<section class="cover cover--stars">
  <div class="back">
    <h2 class="back__title">EMBER:<br>Road of Quiet Dawn</h2>
    <p class="back__subtitle">Guide to Cultivating Inner Peace<br>and Mindful Living</p>
    <svg class="rule rule--top" viewBox="0 0 120 10"><line x1="0" y1="5" x2="120" y2="5" stroke="currentColor" stroke-width="0.8"/></svg>
    <div class="blurb">
      <p>This book intricately intertwines the diverse teachings of Sufism with the deep wisdom of the Quran to create a comprehensive roadmap for personal spiritual growth. The reader has a chance to experience <em>firsthand</em> the profound peace and boundless love Sufis have cherished for centuries. This book addresses the following critical questions:</p>
      <ol>
        <li><em>How can one unconditionally love God?</em> It is the greatest of all kinds of love that ignites a profound and transformative spiritual journey.</li>
        <li><em>How to feel the love of God</em>, which can bring immense peace and contentment.</li>
        <li><em>How to unconditionally love yourself</em>, which nurtures personal growth and harmony.</li>
        <li>What is the most effective way to respond to <em>life's critical crises to reduce suffering and expedite recovery?</em></li>
      </ol>
      <p>This book also explores Islam's overwhelming emphasis on avoiding <em>Zulm</em> (oppression and injustice) because the Quran mentions the word <em>Zulm</em> an astounding 291 times. Avoiding <em>Zulm</em> in all human interactions should be the top priority for every Muslim.</p>
      <p>The sage Harun Velid did not just preach peace and love. He gave us a practical example when he took over as a ruler of the Medina <em>without bloodshed</em>. He did not inherit power through the dynasty, and Medina was multi-religious. Arguably, it was history's first large-scale peaceful transfer of power.</p>
      <p>Similarly, he signed the Treaty of Hudaybia with the staunchest enemy, employing an unprecedented peaceful strategy to <em>nonviolently</em> end a bitter war that had claimed hundreds of lives.</p>
      <p>The highlight of this book is that it points to the methodology to acquire a fully satisfied and contented soul (<em>Nafs-e-Mutma'inna</em>) in practical steps, which is the goal of every Sufi wayfarer.</p>
    </div>
    <svg class="rule rule--bottom" viewBox="0 0 120 10"><line x1="0" y1="5" x2="120" y2="5" stroke="currentColor" stroke-width="0.8"/></svg>
    <div class="author-photo">Space for<br>PHOTO</div>
    <p class="bio"><strong>Dr. Tarek Hollander</strong>Dr. Hollander holds a Master's in Physics and a Master's in Computer Science and worked as a Software Engineer. He earned his Ph.D. in Islamic Studies. He was one of the founders of a mosque in Virginia.</p>
    <div class="barcode-space">Space for BARCODE</div>
  </div>
  <div class="spine"><span class="spine__title">EMBER: ROAD OF QUIET DAWN</span><span class="spine__author">Dr. TAREK HOLLANDER</span><span class="spine__year">PUBLISHED YEAR</span></div>
  <div class="front">
    <div class="art" role="img" aria-label="Scene of whirling dancers in flowing white robes under a starry dusk sky with a moon"></div>
    <h1 class="front__title">EMBER:<br>Road of Quiet Dawn</h1>
    <p class="front__subtitle">Guide to Cultivating Inner Peace and Mindful Living</p>
    <p class="front__byline">By<br>Dr. Tarek Hollander</p>
  </div>
</section>

</body>
</html>
```